Sunset Harbour Living Web Page

We need a web page design that has two intro pages - first being a 'home page', then a link to the second page that has the 'content tabs' and a 'call to action' (see below).

The business helps people that wish to retire to S.E.Asia (Thailand, Malaysia, Indonesia,The Philippines etc) - to enjoy the lifestyle and the remaining years of their lives. What attracts S.E.Asia to many people is the lower cost, the atmoshpere and beauty of the tropics and the vibrancy of the various countries.

People that are wishing to make the most of their retirement and are adventurous at a great bargain compared to the cost of their own countries will be interested.

We help them achieve this - visa, financials (tax, gov't payments etc), introduce them to the right people for property, clubs, retirement facilities, insurance and so forth.

Therefore we are providing an extremely wide ranging service and this site will provide broad but general information only - with a call to action to come and see us for more specific information and how we can help them specifically.

This site will be predominantly for travel and lifestyle, it will be linked with another financial services (financial planning) site later down the track.

The colour scheme is dark green and blue - as per the attached logo design. Photos and background just think lifestyle and S.E.Asia - beaches/mountains/water/recreational activities for retirees.

Target market is mostly those coming up to retirement to those that are already retired. But we also expect to have some interest with younger people that would like to find out more and plan for the future. So a broad age group but I would say mostly 40-70 yrs old.

On the first (Home) page we would like our company name 'Sunset Harbour Living', our logo (which will be on all pages) and a statement such as: “Imagine a retirement where your dreams are brought to life, and you have never felt more alive. Let us show you how”. Then a link to the second page.

We would like an uncluttered site. On the second (contents) page the tabs would be:

- Visa
- Property
- Financials
- Travel
- Insurance & Healthcare
- Medical Tourism
- Cost of living
- Weekly Blogs and articles
- Sunset Harbour Living story

We would also like a call to action on the second page - asking them to leave their contact details if they wish to learn more or sign up to our weekly newsletter/blog.

We are open to suggestions and your imaginations.

Thank you
Gerald

Font styles to use
Serif
Script

Colors
0255a3
3377b5
00a990
9bcb3c
abd036
33b8a4
85abd2
cadf82
86cfc6

Requirements
Must have
• I have been asked by the web designer to receive a 'Web Font' so that we can 'get off of Plixora'. Hope that makes sense.

```html
<!DOCTYPE html>
<html lang="en">
<head>
<meta charset="utf-8">
<title>Sunset Harbour Living</title>
<link rel="stylesheet" href="https://fonts.googleapis.com/css2?family=Exo+2:wght@400;500;600;700&family=Open+Sans:wght@400;600;700&family=Playfair+Display:wght@400;500&family=Great+Vibes&display=swap">
<style>
:root{
  --green:#10a85c;
  --green-dark:#0b8f4c;
  --blue:#1f97d4;
  --blue-deep:#0a8fce;
  --blue-bar:#0b7fb8;
  --text:#444;
  --muted:#666;
  --line:#dcdcdc;
  --white:#fff;
  --grey-icon:#cfcfcf;
}
*{box-sizing:border-box;margin:0;padding:0}
html,body{width:1200px;height:2922px;overflow:hidden}
body{position:relative;background:var(--white);font-family:"Open Sans",Arial,sans-serif;color:var(--text);font-size:14px}
.abs{position:absolute}
a{color:inherit;text-decoration:none}

/* header */
.brand{left:70px;top:38px;display:flex;align-items:center;gap:12px}
.brand-dot{width:70px;height:70px;border-radius:50%;background:var(--green)}
.brand-name{font-family:"Exo 2",sans-serif;font-weight:700;font-size:30px;color:var(--blue);line-height:1.05;width:200px}
.top-links{right:42px;top:12px;display:flex;gap:18px;font-size:13px;color:#555}
.social-top{right:42px;top:52px;display:flex;gap:14px}
.social-top span{width:36px;height:36px;background:var(--grey-icon);display:block}
.contact-box{left:700px;top:113px;width:425px;height:50px;background:var(--blue);border-radius:8px 8px 0 0;display:flex;color:var(--white)}
.contact-box div{flex:1;display:flex;align-items:center;gap:10px;padding-left:16px;font-size:13px;line-height:1.2}
.contact-box div+div{border-left:1px solid rgba(255,255,255,.5)}
.contact-box b{font-weight:700;font-size:14px;display:block}
.ic{width:28px;height:28px;flex:none}

.main-nav{left:0;top:163px;width:1200px;height:42px;background:var(--green);border-bottom:3px solid var(--green-dark);display:flex;padding-left:62px}
.main-nav a{color:var(--white);font-family:"Exo 2",sans-serif;font-weight:500;font-size:13.5px;line-height:39px;padding:0 8px;border-right:1px solid rgba(255,255,255,.45)}
.main-nav a:first-child{border-left:1px solid rgba(255,255,255,.45)}

/* hero */
.hero{left:0;top:205px;width:1200px;height:479px;background:linear-gradient(100deg,#6b4418 0%,#8c5a22 35%,#a87a42 60%,#5d3c17 100%)}
.hero-copy{left:0;top:105px;width:1200px;text-align:center;color:var(--white);font-family:"Playfair Display",serif}
.hero-imagine{font-size:68px;letter-spacing:26px;line-height:1;padding-left:26px}
.hero-rule{position:absolute;height:2px;background:rgba(255,255,255,.85)}
.hero-a{font-family:"Great Vibes",cursive;font-size:40px;line-height:44px}
.hero-main{font-size:50px;line-height:54px;letter-spacing:.5px}
.hero-main i{font-family:"Great Vibes",cursive;font-style:normal;font-size:46px}
.hero-sub{font-size:27px;line-height:34px;margin-top:2px}
.hero-arrow{top:427px;width:34px;height:34px}

/* welcome */
.welcome-title{left:0;top:730px;width:1200px;text-align:center;font-family:"Exo 2",sans-serif;font-weight:600;font-size:23px;color:#222}
.welcome-title span{color:var(--blue)}
.title-mark{left:588px;top:764px;width:24px;height:12px}
.welcome-text{left:100px;top:793px;width:1000px;text-align:center;font-size:14px;line-height:24px;color:var(--muted)}
.btn{display:inline-flex;align-items:center;gap:8px;background:var(--green);color:var(--white);font-family:"Exo 2",sans-serif;font-weight:500;font-size:13px;height:38px;padding:0 16px;border-radius:3px}
.btn svg{width:13px;height:13px}

/* sections */
.sec-title{font-family:"Exo 2",sans-serif;font-weight:600;font-size:17px;color:var(--blue);text-transform:uppercase}
.feature{width:333px}
.feature .sec-title{margin-bottom:20px}
.feature-body{font-size:14px;line-height:24px;color:var(--muted)}
.feature-thumb{float:left;width:117px;height:117px;margin:2px 12px 4px 0}
.feature .btn{margin-top:18px}

.photo{display:block}
.g-finance{background:linear-gradient(135deg,#2f4e70,#8aa4c2)}
.g-health{background:linear-gradient(135deg,#cfd9e4,#6f8aa3)}
.g-house1{background:linear-gradient(180deg,#9cc8ec 0%,#b45b2a 45%,#3c6b2a 100%)}
.g-house2{background:linear-gradient(180deg,#5aa0e0 0%,#7a5a48 50%,#6a7a4a 100%)}
.g-house3{background:linear-gradient(180deg,#bcd6ea 0%,#8a3e22 50%,#4f7a34 100%)}
.g-thai{background:linear-gradient(180deg,#a9d6ee 0%,#6f8a5e 45%,#2fb8b8 75%,#e4dcc0 100%)}
.g-malay{background:linear-gradient(180deg,#1d5fc0 0%,#d04a20 50%,#e8a030 100%)}
.g-video{background:linear-gradient(135deg,#2e5a2a,#7fa05a 50%,#2e3a2a)}
.g-blog{background:linear-gradient(135deg,#c7a98a,#6a8a6a)}
.g-t1{background:linear-gradient(135deg,#6a7d5a,#c6b48a)}
.g-t2{background:linear-gradient(135deg,#f0a050,#4a6a8a)}
.g-t3{background:linear-gradient(135deg,#9cc0dc,#3a7a6a)}
.g-t4{background:linear-gradient(135deg,#8cc8e8,#3aa8b0)}
.g-t5{background:linear-gradient(135deg,#a0d4ec,#2ab0b8)}
.g-t6{background:linear-gradient(135deg,#9cd0ee,#c0504a)}
.g-avatar{background:linear-gradient(135deg,#e2c2a8,#9a7a66)}

.prop-card{width:216px}
.prop-card .photo{height:160px}
.prop-card p{font-size:14px;color:#555;margin-top:6px}

.band{left:74px;top:1676px;width:691px;height:66px;background:var(--blue);color:var(--white);text-align:center;font-family:"Exo 2",sans-serif;font-weight:500;font-size:20px;line-height:24px;padding-top:9px;text-transform:uppercase}

.country{width:333px}
.country .photo{height:182px;margin-top:12px}
.country h4{font-family:"Exo 2",sans-serif;font-weight:600;font-size:15px;color:#222;margin-top:22px}
.country .lede{font-size:13px;line-height:21px;color:var(--muted);margin-top:6px;padding-bottom:18px;border-bottom:1px solid var(--line)}
.mini{display:flex;gap:14px;padding:14px 0 16px;border-bottom:1px solid var(--line)}
.mini:last-child{border-bottom:0}
.mini .photo{width:72px;height:72px;margin:0;flex:none}
.mini b{display:block;font-size:13.5px;color:#222;margin-bottom:4px}
.mini p{font-size:12.5px;line-height:19px;color:var(--muted)}

/* sidebar */
.video-box{left:793px;top:1005px;width:333px;height:280px;border:3px solid var(--blue);background:var(--blue)}
.video-box h3{font-family:"Exo 2",sans-serif;font-weight:600;font-size:16px;color:var(--white);padding:12px 12px 0;height:43px}
.video-box .photo{height:231px}
.play{left:150px;top:147px;width:54px;height:54px}

.tabs-box{left:793px;top:1313px;width:333px;height:398px;border:1px solid var(--line)}
.tabs{display:flex;height:52px;border-bottom:1px solid var(--line)}
.tabs span{flex:1;text-align:center;line-height:52px;font-family:"Exo 2",sans-serif;font-size:17px;color:#333}
.tabs span.on{color:var(--blue);border-right:1px solid var(--line);background:var(--white);margin-bottom:-1px}
.tabs span+span{background:#fafafa}
.blog-item{display:flex;gap:16px;padding:0 18px;margin-top:20px}
.blog-item .photo{width:70px;height:70px;flex:none}
.blog-item b{display:block;font-size:13px;color:#222;margin-bottom:3px}
.blog-item p{font-size:12px;line-height:18px;color:var(--muted)}
.tabs-box .btn{margin:22px 0 0 18px}

.story-box{left:793px;top:1738px;width:333px;height:402px;background:var(--green);border-bottom:4px solid var(--green-dark)}
.story-box h3{font-family:"Exo 2",sans-serif;font-weight:600;font-size:17px;color:var(--white);padding:16px 18px 0;text-transform:uppercase}
.quote{margin:16px 18px 0;background:var(--white);border-radius:6px;height:274px;padding:18px 20px;font-style:italic;font-size:13px;line-height:24px;color:var(--muted)}
.author{display:flex;align-items:center;gap:14px;margin-top:14px;font-style:normal;font-weight:700;color:#333;font-size:13px}
.author .photo{width:64px;height:64px;border-radius:50%}
.story-nav{left:917px;top:2080px;display:flex;gap:10px}
.story-nav svg{width:34px;height:34px}

/* footer */
.footer-wave{left:0;top:2440px;width:1200px;height:120px}
.footer{left:0;top:2550px;width:1200px;height:333px;background:var(--blue-deep);color:var(--white)}
.f-head{font-family:"Exo 2",sans-serif;font-weight:600;font-size:14px;text-transform:uppercase;margin-bottom:18px}
.f-list{list-style:none;font-size:13px;line-height:24px}
.f-text{font-size:13px;line-height:22px}
.f-input{margin-top:16px;width:273px;height:34px;background:var(--white);color:#999;font-size:12px;padding:0 12px;line-height:34px}
.f-btn{margin-top:16px;display:inline-block;background:#3fb2e6;height:32px;line-height:32px;padding:0 16px;font-size:12px;font-weight:700;text-transform:uppercase}
.f-social{display:flex;gap:12px}
.f-social span{width:36px;height:36px;background:#57b8e4;display:block}
.f-contact{display:flex;gap:30px;align-items:center;font-size:17px}
.f-contact span{display:flex;align-items:center;gap:10px}
.f-brand{left:900px;top:180px;width:220px;text-align:center;font-family:"Exo 2",sans-serif;font-weight:700;font-size:27px;line-height:1.15}
.f-brand i{display:block;width:60px;height:60px;border-radius:50%;background:var(--white);margin:0 auto 14px}
.copyright{left:0;top:2883px;width:1200px;height:39px;background:var(--blue-bar);color:var(--white);text-align:center;font-size:13px;line-height:39px}
</style>
</head>
<body>

<header>
  <a class="abs brand" href="#"><span class="brand-dot"></span><span class="brand-name">Sunset Harbour Living</span></a>
  <nav class="abs top-links"><a href="#">HOME</a><a href="#">ABOUT US</a><a href="#">CONTACT US</a></nav>
  <div class="abs social-top" aria-label="Social links"><span></span><span></span><span></span><span></span><span></span></div>
  <div class="abs contact-box">
    <div>
      <svg class="ic" viewBox="0 0 28 28"><circle cx="14" cy="14" r="12.5" fill="none" stroke="#fff" stroke-width="1.5"/><path d="M10 8l3 3-1.6 1.8c.8 1.7 2 2.9 3.8 3.8L17 15l3 3-2 2c-4.5-.5-9.5-5.5-10-10z" fill="#fff"/></svg>
      <span>Call Us:<b>+1-000-000-0000</b></span>
    </div>
    <div>
      <svg class="ic" viewBox="0 0 28 28"><circle cx="14" cy="14" r="12.5" fill="none" stroke="#fff" stroke-width="1.5"/><rect x="8" y="10" width="12" height="9" fill="none" stroke="#fff" stroke-width="1.5"/><path d="M8 10l6 5 6-5" fill="none" stroke="#fff" stroke-width="1.5"/></svg>
      <span>Email Us:<b>info@sunsetharbourliving.com</b></span>
    </div>
  </div>
  <nav class="abs main-nav">
    <a href="#">VISA</a><a href="#">PROPERTY</a><a href="#">FINANCIALS</a><a href="#">TRAVEL</a><a href="#">INSURANCE &amp; HEALTHCARE</a><a href="#">MEDICAL TOURISM</a><a href="#">COST OF LIVING</a><a href="#">WEEKLY BLOGS &amp; ARTICLES</a><a href="#">SUNSET HARBOUR LIVING STORY</a>
  </nav>
</header>

<section class="abs hero" role="img" aria-label="Retired couple walking bicycles along a beach at sunset">
  <div class="abs hero-copy">
    <div class="hero-imagine">IMAGINE</div>
    <div class="hero-a">a</div>
    <div class="hero-main">RETIREMENT WHERE <i>your</i> DREAMS</div>
    <div class="hero-sub">ARE BROUGHT TO LIFE, AND YOU HAVE NEVER FELT MORE ALIVE.</div>
  </div>
  <span class="hero-rule" style="left:170px;top:215px;width:400px"></span>
  <span class="hero-rule" style="left:630px;top:215px;width:403px"></span>
  <span class="hero-rule" style="left:170px;top:358px;width:863px"></span>
  <svg class="abs hero-arrow" style="left:40px" viewBox="0 0 34 34"><circle cx="17" cy="17" r="15" fill="#222" stroke="#fff" stroke-width="2"/><path d="M20 10l-7 7 7 7" fill="none" stroke="#fff" stroke-width="3"/></svg>
  <svg class="abs hero-arrow" style="left:1126px" viewBox="0 0 34 34"><circle cx="17" cy="17" r="15" fill="#222" stroke="#fff" stroke-width="2"/><path d="M14 10l7 7-7 7" fill="none" stroke="#fff" stroke-width="3"/></svg>
</section>

<section>
  <h2 class="abs welcome-title">WELCOME TO <span>SUNSET HARBOUR LIVING</span></h2>
  <svg class="abs title-mark" viewBox="0 0 24 12"><path d="M0 10h24" stroke="#1f97d4" stroke-width="2"/><path d="M6 10a6 6 0 0 1 12 0z" fill="#10a85c"/></svg>
  <p class="abs welcome-text">Lorem ipsum dolor sit amet, consectetur adipiscing elit, sed do eiusmod tempor incididunt ut labore et dolore magna aliqua. Ut enim ad minim veniam, quis nostrud exercitation ullamco laboris nisi ut aliquip ex ea commodo consequat. Duis aute irure dolor in reprehenderit in voluptate velit esse cillum dolore eu fugiat nulla pariatur. Excepteur sint occaecat cupidatat non proident, sunt in culpa qui officia deserunt mollit anim id est laborum.</p>
  <a class="abs btn" style="left:534px;top:913px" href="#">READ MORE <svg viewBox="0 0 13 13"><circle cx="6.5" cy="6.5" r="5.5" fill="none" stroke="#fff"/><path d="M5.5 4l2.5 2.5-2.5 2.5" fill="none" stroke="#fff"/></svg></a>
</section>

<article class="abs feature" style="left:74px;top:1004px">
  <h3 class="sec-title">What about your financial future?</h3>
  <div class="feature-body"><span class="photo feature-thumb g-finance" role="img" aria-label="Businessman using a laptop"></span>Lorem ipsum dolor sit amet, consectetur adipiscing elit, sed do eiusmod tempor incididunt ut labore et dolore magna aliqua. Ut enim ad minim veniam, quis nostrud exercitation ullamco laboris nisi ut aliquip ex ea commodo consequat. Duis aute irure dolor in.</div>
  <a class="btn" href="#">READ MORE <svg viewBox="0 0 13 13"><circle cx="6.5" cy="6.5" r="5.5" fill="none" stroke="#fff"/><path d="M5.5 4l2.5 2.5-2.5 2.5" fill="none" stroke="#fff"/></svg></a>
</article>
<article class="abs feature" style="left:432px;top:1004px">
  <h3 class="sec-title">Insurance &amp; Healthcare</h3>
  <div class="feature-body"><span class="photo feature-thumb g-health" role="img" aria-label="Medical insurance form with stethoscope"></span>Lorem ipsum dolor sit amet, consectetur adipiscing elit, sed do eiusmod tempor incididunt ut labore et dolore magna aliqua. Ut enim ad minim veniam, quis nostrud exercitation ullamco laboris nisi ut aliquip ex ea commodo consequat. Duis aute irure dolor in.</div>
  <a class="btn" href="#">READ MORE <svg viewBox="0 0 13 13"><circle cx="6.5" cy="6.5" r="5.5" fill="none" stroke="#fff"/><path d="M5.5 4l2.5 2.5-2.5 2.5" fill="none" stroke="#fff"/></svg></a>
</article>

<section>
  <h3 class="abs sec-title" style="left:74px;top:1347px">List a property!</h3>
  <div class="abs prop-card" style="left:74px;top:1383px"><span class="photo g-house1" role="img" aria-label="Traditional Thai house with garden"></span><p>Lorem House for Sale</p></div>
  <div class="abs prop-card" style="left:312px;top:1383px"><span class="photo g-house2" role="img" aria-label="Wooden temple-style house under blue sky"></span><p>Lorem House for Sale</p></div>
  <div class="abs prop-card" style="left:550px;top:1383px"><span class="photo g-house3" role="img" aria-label="Teak house surrounded by trees"></span><p>Lorem House for Sale</p></div>
  <a class="abs btn" style="left:74px;top:1583px" href="#">LIST A PROPERTY! <svg viewBox="0 0 13 13"><circle cx="6.5" cy="6.5" r="5.5" fill="none" stroke="#fff"/><path d="M5.5 4l2.5 2.5-2.5 2.5" fill="none" stroke="#fff"/></svg></a>
</section>

<div class="abs band">Enjoy the lifestyle and<br>the remaining years of their lives</div>

<article class="abs country" style="left:74px;top:1766px">
  <h3 class="sec-title">Retire to Thailand</h3>
  <span class="photo g-thai" role="img" aria-label="Limestone island and longtail boat on a tropical beach"></span>
  <h4>LIFESTYLE IN THAILAND</h4>
  <p class="lede">Lorem ipsum dolor sit amet, consectetur adipiscing elit</p>
  <div class="mini"><span class="photo g-t1" role="img" aria-label="Rope bridge in the jungle"></span><div><b>Lorem ipsum dolor sit amet</b><p>Sed ut perspiciatis unde omnis iste natus error sit voluptatem.</p></div></div>
  <div class="mini"><span class="photo g-t2" role="img" aria-label="Sunset over the sea"></span><div><b>Lorem ipsum dolor sit amet</b><p>Sed ut perspiciatis unde omnis iste natus error sit voluptatem.</p></div></div>
  <div class="mini"><span class="photo g-t3" role="img" aria-label="Rock island in a bay"></span><div><b>Lorem ipsum dolor sit amet</b><p>Sed ut perspiciatis unde omnis iste natus error sit voluptatem.</p></div></div>
</article>
<article class="abs country" style="left:432px;top:1766px">
  <h3 class="sec-title">Retire to Malaysia</h3>
  <span class="photo g-malay" role="img" aria-label="Chinese temple with red lanterns"></span>
  <h4>LIFESTYLE IN MALAYSIA</h4>
  <p class="lede">Lorem ipsum dolor sit amet, consectetur adipiscing elit</p>
  <div class="mini"><span class="photo g-t4" role="img" aria-label="Tropical beach with palm trees"></span><div><b>Lorem ipsum dolor sit amet</b><p>Sed ut perspiciatis unde omnis iste natus error sit voluptatem.</p></div></div>
  <div class="mini"><span class="photo g-t5" role="img" aria-label="Clear turquoise lagoon"></span><div><b>Lorem ipsum dolor sit amet</b><p>Sed ut perspiciatis unde omnis iste natus error sit voluptatem.</p></div></div>
  <div class="mini"><span class="photo g-t6" role="img" aria-label="Colourful fishing boat on the shore"></span><div><b>Lorem ipsum dolor sit amet</b><p>Sed ut perspiciatis unde omnis iste natus error sit voluptatem.</p></div></div>
</article>
<a class="abs btn" style="left:353px;top:2375px" href="#">VIEW MORE <svg viewBox="0 0 13 13"><circle cx="6.5" cy="6.5" r="5.5" fill="none" stroke="#fff"/><path d="M5.5 4l2.5 2.5-2.5 2.5" fill="none" stroke="#fff"/></svg></a>

<aside>
  <div class="abs video-box">
    <h3>LISTEN TO WHAT THIS SITE IS ABOUT</h3>
    <span class="photo g-video" role="img" aria-label="Video of a smiling retiree outdoors"></span>
    <svg class="abs play" viewBox="0 0 54 54"><circle cx="27" cy="27" r="24" fill="none" stroke="#10a85c" stroke-width="4"/><path d="M21 16l17 11-17 11z" fill="#10a85c"/></svg>
  </div>
  <div class="abs tabs-box">
    <div class="tabs"><span class="on">WEEKLY BLOGS</span><span>ARTICLES</span></div>
    <div class="blog-item"><span class="photo g-blog" role="img" aria-label="Retired couple outdoors"></span><div><b>Lorem ipsum dolor sit amet</b><p>July 2, 2015, No Comments on Ut enim ad minim veniam.</p></div></div>
    <div class="blog-item"><span class="photo g-blog" role="img" aria-label="Retirees relaxing together"></span><div><b>Lorem ipsum dolor sit amet</b><p>July 2, 2015, No Comments on Ut enim ad minim veniam.</p></div></div>
    <div class="blog-item"><span class="photo g-blog" role="img" aria-label="Older couple on holiday"></span><div><b>Lorem ipsum dolor sit amet</b><p>July 2, 2015, No Comments on Ut enim ad minim veniam.</p></div></div>
    <a class="btn" href="#">READ MORE <svg viewBox="0 0 13 13"><circle cx="6.5" cy="6.5" r="5.5" fill="none" stroke="#fff"/><path d="M5.5 4l2.5 2.5-2.5 2.5" fill="none" stroke="#fff"/></svg></a>
  </div>
  <div class="abs story-box">
    <h3>Sunset Harbour Living Story</h3>
    <div class="quote">“Lorem ipsum dolor sit amet, consectetur adipiscing elit, sed do eiusmod tempor incididunt ut labore et dolore magna aliqua. Ut enim ad minim veniam, quis nostrud exercitation ullamco laboris nisi ut aliquip ex ea commodo”
      <div class="author"><span class="photo g-avatar" role="img" aria-label="Customer portrait"></span>-John Doe</div>
    </div>
  </div>
  <div class="abs story-nav">
    <svg viewBox="0 0 34 34"><circle cx="17" cy="17" r="15" fill="none" stroke="#fff" stroke-width="2.5"/><path d="M19 10l-7 7 7 7M12 17h12" fill="none" stroke="#fff" stroke-width="2.5"/></svg>
    <svg viewBox="0 0 34 34"><circle cx="17" cy="17" r="15" fill="none" stroke="#fff" stroke-width="2.5"/><path d="M15 10l7 7-7 7M22 17H10" fill="none" stroke="#fff" stroke-width="2.5"/></svg>
  </div>
</aside>

<svg class="abs footer-wave" viewBox="0 0 1200 120" preserveAspectRatio="none"><path d="M0 30 C80 10 150 50 230 35 S400 60 480 45 S560 20 620 50 S760 40 840 55 S980 30 1060 45 S1160 35 1200 40 V120 H0z" fill="#0a8fce"/></svg>
<footer class="abs footer">
  <div class="abs" style="left:74px;top:50px"><h4 class="f-head">Quick Links</h4>
    <ul class="f-list"><li>Visa</li><li>Property</li><li>Financials</li><li>Travel</li><li>Insurance &amp; Healthcare</li></ul></div>
  <div class="abs" style="left:228px;top:86px"><ul class="f-list"><li>Medical Tourism</li><li>Cost of living</li><li>Weekly Blogs &amp; articles</li><li>Sunset Harbour story</li></ul></div>
  <div class="abs" style="left:407px;top:50px"><h4 class="f-head">More Links</h4>
    <ul class="f-list"><li>Careers</li><li>Privacy Policy</li><li>Terms And Conditions</li><li>Traveler Resources</li></ul></div>
  <div class="abs" style="left:575px;top:50px;width:300px"><h4 class="f-head">Subscribe to our newsletter</h4>
    <p class="f-text">Keep up to date with our new hire products and special offers</p>
    <div class="f-input">Enter your email address</div>
    <span class="f-btn">Subscribe</span></div>
  <div class="abs" style="left:884px;top:50px"><h4 class="f-head">Follow Us</h4>
    <div class="f-social"><span></span><span></span><span></span><span></span><span></span></div></div>
  <div class="abs f-brand"><i></i>Sunset Harbour Living</div>
  <div class="abs" style="left:74px;top:258px"><h4 class="f-head" style="margin-bottom:12px">Contact Us</h4>
    <div class="f-contact">
      <span><svg class="ic" viewBox="0 0 28 28"><circle cx="14" cy="14" r="12.5" fill="none" stroke="#fff" stroke-width="1.5"/><path d="M10 8l3 3-1.6 1.8c.8 1.7 2 2.9 3.8 3.8L17 15l3 3-2 2c-4.5-.5-9.5-5.5-10-10z" fill="#fff"/></svg>+1-000-000-0000</span>
      <span><svg class="ic" viewBox="0 0 28 28"><circle cx="14" cy="14" r="12.5" fill="none" stroke="#fff" stroke-width="1.5"/><rect x="8" y="10" width="12" height="9" fill="none" stroke="#fff" stroke-width="1.5"/><path d="M8 10l6 5 6-5" fill="none" stroke="#fff" stroke-width="1.5"/></svg>info@sunsetharbourliving.com</span>
    </div></div>
</footer>
<div class="abs copyright">© 2016 Sunset Harbour Living. All Rights Reserved</div>

</body>
</html>
```